New Business Card Design Project

Hi there

Could you please make a design that is soft and appealing to people who would purchase gemstones, buy healing jewellery, seek counselling, may seek energy healing and/or learn English. Essentially I'm looking for something with a soft human design. Please incorporate the logo and select font that can be easily read and softer images in the background - but not too busy. I would like it double sided as well.

Optional: Elements could include gemstones, feathers, plants and images that are happy and calming.

Target Market(s)

People into alternative health, those from non-English speaking backgrounds, businesses

Contact Information for Business Card

Lena Whitford
Mobile: 0418 265 093, Facebook and Instagram Logos,
ABN: 61 472 185 034 (Australian Business Number - small at the bottom)

Requirements
Must have
• My project must have:
- Meadow Thread logo
- Symbols that represent the 4 main services: 1. Gemstones/jewellery, 2. counselling, 3. meditation/energy healing, 4. education
Nice to have
• Clear and easy to read.

```html
<!DOCTYPE html>
<html lang="en">
<head>
<meta charset="utf-8">
<title>Meadow Thread – Business Card</title>
<link href="https://fonts.googleapis.com/css2?family=Montserrat:wght@400;500;700&display=swap" rel="stylesheet">
<style>
  :root {
    --backdrop: #b0b0ab;
    --card-white: #ffffff;
    --teal: #2bb5a8;
    --teal-soft: #d6f1ee;
    --leaf-green: #6aaa1e;
    --ink: #3a3a3a;
    --white: #ffffff;
  }
  * { box-sizing: border-box; margin: 0; padding: 0; }
  html, body {
    width: 1200px; height: 801px; overflow: hidden;
    background: var(--backdrop);
    font-family: "Montserrat", sans-serif;
  }
  .stage {
    position: relative; width: 1200px; height: 801px;
    display: flex; align-items: center; justify-content: center; gap: 40px;
  }
  .card {
    position: relative; width: 540px; height: 310px;
    border-bottom: 5px solid var(--leaf-green);
    box-shadow: 0 10px 24px rgba(0,0,0,0.18);
    overflow: hidden;
  }
  /* Front side */
  .card--front { background: var(--card-white); }
  .front__decor {
    position: absolute; right: -60px; top: -80px;
    width: 330px; height: 330px; border-radius: 50%;
    background: radial-gradient(circle, var(--teal-soft) 0%, rgba(214,241,238,0.4) 70%, rgba(255,255,255,0) 100%);
  }
  .brand {
    position: absolute; left: 36px; top: 60px;
  }
  .brand__name {
    font-weight: 500; font-size: 30px; letter-spacing: 2px;
    color: var(--leaf-green); text-transform: uppercase; line-height: 1;
  }
  .brand__rule {
    width: 250px; height: 2px; background: var(--teal); margin: 10px 0 8px;
  }
  .brand__abn { font-size: 12px; color: var(--ink); }
  .brand__abn span { color: var(--leaf-green); font-weight: 500; }
  .person {
    position: absolute; left: 36px; top: 170px;
  }
  .person__name {
    font-weight: 700; font-size: 21px; letter-spacing: 1px;
    color: var(--leaf-green); text-transform: uppercase;
  }
  .person__role { font-size: 13px; color: var(--ink); margin-top: 2px; }
  .contact { list-style: none; margin-top: 12px; }
  .contact__item {
    display: flex; align-items: center; gap: 8px;
    font-size: 13px; color: var(--ink); line-height: 20px;
  }
  .contact__icon { width: 11px; height: 11px; flex: none; }
  .front__tab {
    position: absolute; left: 0; bottom: 0; width: 16px; height: 22px;
    background: var(--leaf-green);
  }
  /* Back side */
  .card--back {
    background: var(--teal);
    display: flex; flex-direction: column; align-items: center; justify-content: center;
    color: var(--white);
  }
  .back__brand {
    font-weight: 500; font-size: 40px; letter-spacing: 3px;
    text-transform: uppercase; line-height: 1;
  }
  .back__rule { width: 320px; height: 2px; background: var(--white); margin: 14px 0 24px; }
  .services {
    list-style: none; display: grid; grid-template-columns: auto auto;
    column-gap: 26px; row-gap: 8px;
  }
  .services__item {
    display: flex; align-items: center; gap: 8px; font-size: 15px; font-weight: 500;
  }
  .services__icon { width: 16px; height: 16px; flex: none; }
</style>
</head>
<body>
<main class="stage">
  <section class="card card--front" aria-label="Business card front">
    <div class="front__decor" role="img" aria-label="Large soft brand decoration in teal"></div>
    <div class="brand">
      <div class="brand__name">Meadow Thread</div>
      <div class="brand__rule"></div>
      <div class="brand__abn"><span>ABN:</span> 61 472 185 034</div>
    </div>
    <div class="person">
      <div class="person__name">Lena Whitford</div>
      <div class="person__role">Founder</div>
      <ul class="contact">
        <li class="contact__item">
          <svg class="contact__icon" viewBox="0 0 12 12"><path d="M3 1 L5 3 L4 5 Q5 7 7 8 L9 7 L11 9 L9 11 Q2 10 1 3 Z" fill="#6aaa1e"/></svg>
          0418 265 093
        </li>
        <li class="contact__item">
          <svg class="contact__icon" viewBox="0 0 12 12"><rect x="1" y="2.5" width="10" height="7" fill="none" stroke="#6aaa1e" stroke-width="1.3"/><path d="M1 2.5 L6 6.5 L11 2.5" fill="none" stroke="#6aaa1e" stroke-width="1.3"/></svg>
          info@meadowthread.com
        </li>
        <li class="contact__item">
          <svg class="contact__icon" viewBox="0 0 12 12"><circle cx="6" cy="6" r="5" fill="none" stroke="#6aaa1e" stroke-width="1.3"/><path d="M1 6 H11 M6 1 Q3 6 6 11 M6 1 Q9 6 6 11" fill="none" stroke="#6aaa1e" stroke-width="1"/></svg>
          www.meadowthread.com
        </li>
      </ul>
    </div>
    <div class="front__tab"></div>
  </section>

  <section class="card card--back" aria-label="Business card back">
    <div class="back__brand">Meadow Thread</div>
    <div class="back__rule"></div>
    <ul class="services">
      <li class="services__item">
        <svg class="services__icon" viewBox="0 0 16 16"><circle cx="8" cy="8" r="7" fill="none" stroke="#fff" stroke-width="1.2"/><path d="M4.5 6.5 L6 4.5 H10 L11.5 6.5 L8 11.5 Z" fill="none" stroke="#fff" stroke-width="1"/></svg>
        Gemstones/Jewellery
      </li>
      <li class="services__item">
        <svg class="services__icon" viewBox="0 0 16 16"><circle cx="8" cy="8" r="7" fill="none" stroke="#fff" stroke-width="1.2"/><rect x="4" y="5" width="5" height="3.5" rx="1" fill="none" stroke="#fff"/><rect x="7" y="8" width="5" height="3.5" rx="1" fill="none" stroke="#fff"/></svg>
        Counselling
      </li>
      <li class="services__item">
        <svg class="services__icon" viewBox="0 0 16 16"><circle cx="8" cy="8" r="7" fill="none" stroke="#fff" stroke-width="1.2"/><circle cx="8" cy="5" r="1.3" fill="#fff"/><path d="M4 11 Q8 8 12 11 M8 7 V10" fill="none" stroke="#fff"/></svg>
        Meditation/Energy Healing
      </li>
      <li class="services__item">
        <svg class="services__icon" viewBox="0 0 16 16"><circle cx="8" cy="8" r="7" fill="none" stroke="#fff" stroke-width="1.2"/><path d="M4 5 L8 6 L12 5 V11 L8 12 L4 11 Z M8 6 V12" fill="none" stroke="#fff"/></svg>
        Education
      </li>
    </ul>
  </section>
</main>
</body>
</html>
```